依頼概要
■依頼の目的/概要
遊技業組合のポスターデザインの制作をお願いします。
パチンコ店の出玉を換金せずにお楽しみ袋と交換して家に持ち帰ってもらうよう呼びかけるポスターです。。
カウンター前にお楽しみ袋が積まれたワゴンを設置(添付PDF)
店内にポスターを貼ります。

■依頼詳細
過去の制作は26年1月はポスター。26年12月はPOPスタンドパネル。27年はのぼり、昨年28年12月はポスターを制作。
http://www.hanamizu-kumiai.jp/event/index.cgi

・パチンコ・スロットのホール内に掲示します。
・ホール内で目につくカラー・デザインをお願いします。
・社会を風刺作品や今年の流行をとり入れていただくなど。

■原稿内容
・カラー B2ポスター
・景品持ち帰り推進運動
・平成29年12月16日(土)~平成29年1月24日(日)
・山並遊興事業協同組合
コピーはお任せいたします。

その他何かご不明な点がございましたら、お気軽にご質問下さい。
よろしくお願いいたします。
■ 選んだ理由

大変お待たせしました。
どのデザインも好評でしたが目に留まることで選ばれました。
ありがとうございました。 森下

■ 提案者全員のお礼・コメント

たくさんの提案ありがとうございました。
ありがとうございました。 森下

```html
<!DOCTYPE html>
<html lang="ja">
<head>
<meta charset="utf-8">
<title>景品持ち帰り推進運動</title>
<link rel="stylesheet" href="https://fonts.googleapis.com/css2?family=Noto+Sans+JP:wght@500;700;900&display=swap">
<style>
  :root {
    --poster-yellow: #ffe800;
    --ink: #1c1c1c;
    --accent-red: #d7262c;
    --scene-red: #c8322e;
    --scene-cream: #f3e3c6;
    --scene-pink: #e88a8a;
  }
  html, body { margin: 0; padding: 0; overflow: hidden; }
  body { width: 848px; height: 1200px; }
  .poster {
    position: relative;
    width: 848px;
    height: 1200px;
    background: var(--poster-yellow);
    font-family: "Noto Sans JP", sans-serif;
    color: var(--ink);
    overflow: hidden;
  }
  .vertical {
    position: absolute;
    writing-mode: vertical-rl;
    text-orientation: upright;
    margin: 0;
    line-height: 1;
    white-space: nowrap;
  }
  .tcy { text-combine-upright: all; }
  .greeting { font-weight: 900; font-size: 60px; }
  .greeting--first  { left: 664px; top: 28px; }
  .greeting--second { left: 574px; top: 84px; }
  .greeting--third  { left: 482px; top: 184px; font-size: 54px; }
  .period {
    left: 118px; top: 28px;
    font-weight: 900; font-size: 28px; color: var(--accent-red);
  }
  .campaign-title {
    left: 26px; top: 110px;
    font-weight: 900; font-size: 86px; letter-spacing: -1px;
  }
  .illustration {
    position: absolute;
    left: 176px; top: 590px;
    width: 600px; height: 520px;
  }
  .speech {
    left: 690px; top: 410px;
    font-weight: 700; font-size: 26px;
  }
  .organizer {
    position: absolute;
    left: 0; right: 0; top: 1126px;
    display: flex; justify-content: center; align-items: center; gap: 18px;
  }
  .organizer__mark {
    width: 48px; height: 48px; border-radius: 50%;
    background: var(--ink);
  }
  .organizer__text { text-align: center; font-weight: 700; line-height: 1.2; }
  .organizer__name { font-size: 28px; display: block; }
  .organizer__web { font-size: 17px; display: block; letter-spacing: 1px; }
</style>
</head>
<body>
<main class="poster">
  <p class="vertical greeting greeting--first">おおきに</p>
  <p class="vertical greeting greeting--second">またお持ち帰り</p>
  <p class="vertical greeting greeting--third">おたの申します</p>

  <p class="vertical period">平成<span class="tcy">29</span>年<span class="tcy">12</span>月<span class="tcy">16</span>日(土)～平成<span class="tcy">30</span>年<span class="tcy">1</span>月<span class="tcy">24</span>日(日)</p>
  <h1 class="vertical campaign-title">景品持ち帰り推進運動</h1>

  <svg class="illustration" viewBox="0 0 600 520" role="img" aria-label="赤い縁台に並んで座る二人の舞妓のイラスト。一人はお楽しみ袋、もう一人は景品の箱を抱えている">
    <defs>
      <linearGradient id="sceneTone" x1="0" y1="0" x2="0" y2="1">
        <stop offset="0" stop-color="var(--scene-cream)"/>
        <stop offset="0.55" stop-color="var(--scene-pink)"/>
        <stop offset="1" stop-color="var(--scene-red)"/>
      </linearGradient>
    </defs>
    <rect x="0" y="0" width="600" height="520" rx="24" fill="url(#sceneTone)" opacity="0.85"/>
  </svg>
  <p class="vertical speech">楽しみやわぁ</p>

  <footer class="organizer">
    <span class="organizer__mark"></span>
    <span class="organizer__text">
      <span class="organizer__name">山並遊興事業協同組合</span>
      <span class="organizer__web">HANAMIZU-KUMIAI.JP</span>
    </span>
  </footer>
</main>
</body>
</html>
```